Affiliate website design and wireframe

We need a design of an affiliate website for an application we purchased, it is important that you build the website pages according to the developer of the applications specifications (please see attached documents) the developer of the application will configure the pages and add them to the site. Please take special note of his comments below.

We all so need you to create a wire frame so the developer can test everything (http://quartz.lomeriva.vn/)

It will be the homepage and about 16 inner pages (please see attached files)
Here is our website http://maplecourtlink.com/affiliate/affiliates/index.php

The version of the software we purchased is the Quill Partner Grid version

Comments from the developers

1. I will need the source files of the design (photoshop .psd files and font files if custom fonts are used), since the implementation is closely bound to component sizes (like border width, margin width etc.) and colors. If you own a corporate design manual, it's crucial to send it as well. Also, please, make sure if you use custom fonts, that these allow legal website integration (like zorvix web fonts).

2. Any and every content is controlled via templates. All editing/adding/removing etc. is done here. The template files are essentially html/php documents, they use a template engine called brisko (http://www.brisko.net/) which has it's own language similar to php.

3. .psd files are ideal, because we deal with the specifics of QPS/QPG implementation on a daily basis. Any html/css developed in advance may prove to be a poor choice. You may choose to let an in-house developer do the job, but experience wise this is more costly, since he will not be accustomed to the template/functionality systems of QPS/QPG.

4. I will need the source files of the design (photoshop .psd files and font files if custom fonts are used), since the implementation is closely bound to component sizes (like border width, margin width etc.) and colors. If you own a corporate design manual, it's crucial to send it as well. Also, please, make sure if you use custom fonts, that these allow legal website integration (like zorvix web fonts).

Regards,

Tomas Vereck

We prefer illustrations more than pictures of real people.

This is the home page, it is asking for Merchant and Affiliate sign up, not just affiliate.

http://maplecourtlink.com/affiliate/index.php

Please note the home page features both Merchant and Affiliate sign up

We are looking for illustration design not just stock images

Please remember the search menu that searches for the available programs, see the example we gave you, look at the search menu at the top of the page http://www.tradolink.com/

We are reviewing everything, no need to send more designs

Target Market(s)

Natural Products Manufacturers
Natural products Sales reps
Natural Products Bloggers
Social Marketing

Industry/Entity Type

Software

Requirements
Must have
• 1. All links on pages should go to the appropriate pages.
2. Colors can be based on our logo design (look at the attachments)
3. Here is our website http://maplecourtlink.com/affiliate/affiliates/index.php
4. We have attached a drawing of how we think the homepage concept should follow.
5. Main concept of design, is trying to show our sales people (Affiliates) are doing multiple things to advertise and sell the merchants products.(see logo)
6. Need to be able to edit all text and images.
7. Our target audience is Natural product sales people (Advertisers, bloggers, ext) and natural product manufacturers.
8. You can speak to the company who made the application, through live chat, on there website http://www.quillpartnergrid.com/
Nice to have
• See Attached Documents.
site should take up whole website pages
Look For fun Illustrated Website, one of the better ones we have seen is http://www.tradolink.com/index.cfm
Should not have
• Please look very carefully at developers comment above.

```html
<!DOCTYPE html>
<html lang="en">
<head>
<meta charset="utf-8">
<title>Maple Court Link – Affiliate Network</title>
<link rel="stylesheet" href="https://fonts.googleapis.com/css2?family=Roboto+Condensed:wght@400;700&family=Open+Sans:wght@400;600&family=Roboto:wght@300;400;700&display=swap">
<style>
  :root {
    --green: #5aa50e;
    --blue: #0b4a8e;
    --blue-deep: #0a3f7c;
    --blue-band: #0a62ad;
    --header-bg: #f4f5f4;
    --nav-text: #555a5e;
    --nav-line: #6d7174;
    --panel-bg: #f8f8f8;
    --art-warm: #e8c78c;
    --art-soft: #efe3cb;
    --dot: #6f6f6f;
    --btn-light: #f1f2f3;
    --btn-mid: #c9ccd0;
    --btn-text: #6b6f73;
  }
  * { box-sizing: border-box; margin: 0; padding: 0; }
  html, body { width: 1200px; height: 992px; overflow: hidden; background: #fff; }
  body { position: relative; font-family: "Open Sans", Arial, sans-serif; }
  a { text-decoration: none; }

  .site-header { position: absolute; left: 0; top: 0; width: 1200px; height: 206px; background: var(--header-bg); }

  .brand { position: absolute; left: 143px; top: 74px; display: flex; align-items: center; gap: 10px; }
  .brand-mark { width: 26px; height: 26px; border-radius: 50%; background: var(--blue); }
  .brand-name { font-family: "Roboto Condensed", sans-serif; font-weight: 700; font-size: 30px; color: var(--green); letter-spacing: 0.5px; }

  .login { position: absolute; top: 24px; height: 39px; width: 152px; border-radius: 4px; color: #fff; font-family: "Roboto", sans-serif; font-weight: 700; font-size: 13px; display: flex; align-items: center; justify-content: center; }
  .login-affiliate { left: 740px; background: var(--blue); }
  .login-merchant { left: 900px; background: var(--green); }

  .main-nav { position: absolute; left: 585px; top: 94px; width: 461px; height: 30px; border-bottom: 3px solid var(--nav-line); display: flex; justify-content: space-between; }
  .main-nav a { font-family: "Roboto Condensed", sans-serif; font-weight: 700; font-size: 17px; color: var(--nav-text); line-height: 22px; padding: 0 2px; }
  .main-nav a.active { color: var(--green); border-bottom: 3px solid var(--green); margin-bottom: -3px; }

  .map-band { position: absolute; left: 0; top: 232px; width: 1200px; height: 421px; background: linear-gradient(180deg, #0b68b6 0%, var(--blue-band) 60%, #08549a 100%); }

  .category-bar { position: absolute; left: 140px; top: 149px; width: 923px; height: 57px; display: flex; background: linear-gradient(180deg, #1f73c0 0%, #0c4f97 55%, #0a3f7c 100%); border: 1px solid #0a3b73; }
  .category-bar a { color: #fff; font-family: "Roboto Condensed", sans-serif; font-weight: 700; font-size: 15px; line-height: 17px; padding: 10px 0 0 19px; border-right: 1px solid #2b6fb0; }
  .category-bar a:last-child { border-right: none; }

  .hero { position: absolute; left: 140px; top: 206px; width: 923px; height: 474px; background: var(--panel-bg); box-shadow: 0 18px 26px -14px rgba(0,0,0,0.45); overflow: hidden; }
  .hero-art { position: absolute; inset: 0; background: radial-gradient(ellipse 60% 62% at 50% 50%, var(--art-warm) 0%, var(--art-soft) 38%, #f3f3f1 70%, var(--panel-bg) 100%); }

  .slider-dots { position: absolute; left: 553px; top: 724px; display: flex; gap: 6px; }
  .slider-dots span { width: 14px; height: 14px; border-radius: 50%; background: var(--dot); }
  .slider-dots span.current { background: #fff; border: 3px solid var(--dot); }

  .promo { position: absolute; top: 776px; height: 200px; width: 449px; border-radius: 3px; color: #fff; padding: 18px 22px; }
  .promo-affiliate { left: 140px; background: var(--green); }
  .promo-merchant { left: 615px; width: 448px; background: linear-gradient(180deg, #0e4c92 0%, var(--blue-deep) 100%); }
  .promo h2 { font-family: "Roboto Condensed", sans-serif; font-weight: 400; font-size: 31px; line-height: 34px; margin-bottom: 9px; }
  .promo p { font-size: 14.5px; line-height: 17px; width: 390px; }
  .promo-merchant p { width: 416px; }
  .signup { position: absolute; left: 22px; top: 131px; height: 46px; width: 265px; border-radius: 5px; background: linear-gradient(180deg, var(--btn-light) 0%, var(--btn-mid) 100%); display: flex; }
  .signup-label { flex: 1; display: flex; align-items: center; justify-content: center; font-family: "Roboto", sans-serif; font-weight: 700; font-size: 18px; color: var(--btn-text); letter-spacing: 0.5px; border-right: 1px solid #9ea2a6; }
  .signup-icon { width: 48px; display: flex; align-items: center; justify-content: center; }
</style>
</head>
<body>
  <header class="site-header">
    <a class="brand" href="#">
      <span class="brand-mark"></span>
      <span class="brand-name">MAPLE COURT LINK</span>
    </a>
    <a class="login login-affiliate" href="#">AFFILIATE LOGIN</a>
    <a class="login login-merchant" href="#">MERCHANT LOGIN</a>
    <nav class="main-nav">
      <a class="active" href="#">HOME</a>
      <a href="#">ABOUT US</a>
      <a href="#">FAQ</a>
      <a href="#">TESTIMONIAL</a>
      <a href="#">CONTACT US</a>
    </nav>
  </header>

  <div class="map-band" role="img" aria-label="Blue band with a faint world map"></div>

  <nav class="category-bar">
    <a href="#" style="width:172px">NATURAL PRODUCT<br>MERCHANTS</a>
    <a href="#" style="width:155px">GREEN WEBSITE<br>MERCHANTS</a>
    <a href="#" style="width:132px">APPAREL<br>MERCHANTS</a>
    <a href="#" style="width:197px">HOUSEHOLD PRODUCT<br>MERCHANTS</a>
    <a href="#" style="width:144px">FOOD SERVICE<br>MERCHANTS</a>
    <a href="#" style="width:121px">ALL<br>MERCHANTS</a>
  </nav>

  <section class="hero">
    <div class="hero-art" role="img" aria-label="Illustration: natural products (dried fruit pack, bottles, supplement jar, tea box, woven bag) in the centre, with arrows pointing out to labelled marketing channels: blogs, social networks, phone calls, mails, text messages and banner ads"></div>
  </section>

  <div class="slider-dots">
    <span class="current"></span><span></span><span></span><span></span><span></span>
  </div>

  <section class="promo promo-affiliate">
    <h2>START MAKING MONEY NOW</h2>
    <p>There is no charge to join our Affiliate Program. We pay commission for al sales you referred. Earn upto 30% commission.</p>
    <a class="signup" href="#">
      <span class="signup-label">AFFILIATES SIGNUP</span>
      <span class="signup-icon">
        <svg width="26" height="26" viewBox="0 0 26 26" aria-hidden="true"><circle cx="13" cy="13" r="11" fill="#6e7276"/><circle cx="13" cy="13" r="8.5" fill="none" stroke="#e4e6e8" stroke-width="1"/><path d="M7.5 13h9M13 9l4 4-4 4" stroke="#fff" stroke-width="2" fill="none"/></svg>
      </span>
    </a>
  </section>

  <section class="promo promo-merchant">
    <h2>FOR MERCHANTS</h2>
    <p>Lorem ipsum dolor sit amet, consectetur adipiscing elit. Vest ibulum rutrum consequat diam, et sagittis lorem vestibulum sed. Curabitur ac arcu eget augue.</p>
    <a class="signup" href="#">
      <span class="signup-label">MERCHANT SIGNUP</span>
      <span class="signup-icon">
        <svg width="26" height="26" viewBox="0 0 26 26" aria-hidden="true"><circle cx="13" cy="13" r="11" fill="#6e7276"/><circle cx="13" cy="13" r="8.5" fill="none" stroke="#e4e6e8" stroke-width="1"/><path d="M7.5 13h9M13 9l4 4-4 4" stroke="#fff" stroke-width="2" fill="none"/></svg>
      </span>
    </a>
  </section>
</body>
</html>
```